Re-design a highly converting profile page for my website

My website allows people to book a mentor for long-term mentorship as well as sessions. I would like to re-design this site within our branding guidelines to give people the best profile possible.

Please give this website a modern look and concentrate on the CTA and conversion rates. This is a highly converting site and it should stay that way or even get better!

Please also keep menu bar & footer in tact

Target Market(s)

Developers, Designers, Entrepreneurs in the Tech industry

Number of Pages Required

1 page

Requirements
Must have
• Strong CTA, existing color palette, testimonials and major elements
Nice to have
• Modern look, easy to see CTA, easy to scan offer. Not too crowded
Should not have
• No reporpusing. It is and stays a profile page

```html
<!DOCTYPE html>
<html lang="en">
<head>
<meta charset="utf-8">
<title>Evan Marlow – Mentor Profile</title>
<link href="https://fonts.googleapis.com/css2?family=Poppins:wght@300;400;500;600&display=swap" rel="stylesheet">
<style>
:root{
  --teal:#1bd0b2;
  --teal-dark:#13b89c;
  --teal-soft:#f1fcfa;
  --ink:#2c3a4f;
  --text:#5b6472;
  --line:#e6ecef;
  --blue:#2f8cf0;
  --footer:#2f3b57;
  --star:#f6c417;
}
*{box-sizing:border-box;margin:0;padding:0}
html,body{width:1200px;height:3566px;overflow:hidden}
body{position:relative;font-family:'Poppins',sans-serif;color:var(--text);background:#fff;font-size:12.5px}
a{color:var(--teal);text-decoration:none}
.abs{position:absolute}

/* header */
.topbar{position:absolute;left:0;top:0;width:1200px;height:60px;background:#fff}
.brand{position:absolute;left:61px;top:8px;display:flex;align-items:center;gap:10px}
.brand-dot{width:44px;height:44px;border-radius:50%;background:var(--teal)}
.brand-name{font-weight:600;font-size:15px;color:var(--ink)}
.nav{position:absolute;top:24px;font-size:12.5px;color:var(--ink)}
.logout{position:absolute;left:1049px;top:14px;width:90px;height:33px;background:var(--teal);color:#fff;font-weight:500;font-size:15px;border-radius:3px;display:flex;align-items:center;justify-content:center}

/* hero */
.hero{position:absolute;left:0;top:60px;width:1200px;height:285px;background:linear-gradient(160deg,#28d3b8 0%,#19c9ad 55%,#20cdb3 100%)}
.avatar{position:absolute;border-radius:50%;background:linear-gradient(145deg,#d9a98a,#b9715a)}
.hero .avatar{left:190px;top:56px;width:118px;height:118px;border:4px solid #fff}
.hero-name{position:absolute;left:338px;top:58px;font-size:20px;font-weight:500;color:#2c4a5a}
.hero-loc{position:absolute;left:338px;top:90px;color:#fff;font-size:12.5px;display:flex;gap:6px;align-items:center}
.hero-stars{position:absolute;left:338px;top:122px;display:flex;gap:2px;align-items:center;color:#fff;font-size:13px}
.hero-role{position:absolute;left:340px;top:149px;color:#fff;font-size:12px}
.spots{position:absolute;left:870px;top:61px;width:150px;text-align:right;font-weight:600;font-size:13px;color:#2c4a5a;letter-spacing:.5px}
.social{position:absolute;width:38px;height:38px;border-radius:50%;display:flex;align-items:center;justify-content:center}
.social span{width:8px;height:8px;border-radius:50%;background:#fff}
.tab{position:absolute;top:204px;height:36px;background:#1d3346;color:#fff;border-radius:4px;display:flex;align-items:center;gap:12px;padding-left:14px;font-size:12px;font-weight:500}

/* cards */
.card{position:absolute;background:#fff;border:1px solid var(--line);border-radius:4px;box-shadow:0 2px 10px rgba(40,60,80,.05)}
.about{left:165px;top:392px;width:598px;height:1673px;padding:37px 38px 0 38px;line-height:22.5px;font-size:11.8px}
.about p{margin-bottom:23px}
.t-head{position:relative;height:36px;margin:8px 0 42px 0}
.t-badge{position:absolute;left:0;top:0;width:134px;height:36px;background:var(--teal);color:#fff;font-size:15px;display:flex;align-items:center;justify-content:center;border-radius:2px}
.t-rule{position:absolute;left:134px;right:24px;top:18px;border-top:1px solid var(--teal)}
.quote{margin-bottom:12px}
.quote-by{color:var(--ink);font-weight:500;font-size:13.5px;margin-bottom:38px;display:flex;align-items:center;gap:10px}
.quote-by:before{content:"";width:12px;border-top:2px solid var(--teal)}
.promo{border:1px solid var(--teal);background:var(--teal-soft);border-radius:3px;padding:24px 34px;height:164px;margin:0 -2px 44px 0;font-size:12.5px;line-height:22px;color:var(--ink)}
.promo .lead{font-size:14px;margin-bottom:4px}
.promo a{font-weight:500;font-size:13px;display:block;margin:10px 0 4px}
.links{color:var(--ink);font-size:12px;line-height:22px}
.links .gap{height:12px}

.rev{left:165px;width:598px;padding:36px 38px;font-size:11.5px;line-height:21px}
.rev-by{margin-top:14px;display:flex;align-items:center;gap:12px;color:var(--ink);font-weight:500;font-size:12px}

.side{left:785px;width:252px;padding:36px 40px;background:var(--teal-soft);border-color:#bfeee4}
.side h3{font-size:16px;font-weight:500;color:var(--ink);line-height:22px}
.side .small{font-size:11.5px;line-height:19px;color:var(--text)}
.btn{display:inline-flex;align-items:center;justify-content:center;height:36px;background:var(--teal);color:#fff;font-weight:500;font-size:13.5px;border-radius:4px}
.skills{list-style:none;margin-top:26px}
.skills li{height:35px;font-size:12px;font-weight:500;color:var(--ink);display:flex;align-items:center;gap:20px}
.skills li:before{content:"";width:5px;height:5px;border-radius:50%;background:var(--teal)}
.skills li:first-child{color:#99a2ac;font-weight:400}

.related-title{position:absolute;left:166px;top:2825px;font-size:27px;font-weight:500;color:#2c4a6a}
.mentor{top:2882px;width:288px;height:323px;overflow:hidden;padding:0}
.mentor .avatar{left:18px;top:30px;width:44px;height:44px}
.mentor-name{position:absolute;left:70px;top:34px;font-size:17px;font-weight:500;color:var(--ink)}
.mentor-role{position:absolute;left:70px;top:60px;font-size:12px;line-height:18px}
.price{position:absolute;left:200px;top:-12px;width:94px;height:94px;border-radius:50%;background:var(--teal);color:#fff;font-weight:600;font-size:13px;line-height:15px;text-align:center;display:flex;align-items:center;justify-content:center}
.mentor-copy{position:absolute;left:20px;top:110px;width:230px;font-size:11.5px;line-height:20px}
.mentor-list{position:absolute;left:20px;top:172px;list-style:none}
.mentor-list li{height:29px;font-size:11.5px;display:flex;align-items:center;gap:12px}
.mentor-list li:before{content:"";width:4px;height:4px;border-radius:50%;background:var(--teal)}

/* footer */
.footer{position:absolute;left:0;top:3284px;width:1200px;height:267px;background:var(--footer);color:#c9d1dd;font-size:11.5px}
.footer h4{position:absolute;top:51px;color:#fff;font-size:15px;font-weight:500}
.footer ul{position:absolute;top:84px;list-style:none}
.footer li{height:21px;display:flex;align-items:center;gap:12px}
.footer li:before{content:"";width:4px;height:4px;border-radius:50%;background:var(--teal)}
.footstrip{position:absolute;left:0;top:3551px;width:1200px;height:15px;background:var(--teal)}
</style>
</head>
<body>

<header class="topbar">
  <div class="brand"><div class="brand-dot"></div><span class="brand-name">Mentor Harbor</span></div>
  <span class="nav" style="left:739px">Dashboard</span>
  <span class="nav" style="left:826px">Management</span>
  <span class="nav" style="left:926px">Your Profile</span>
  <svg class="abs" style="left:1020px;top:22px" width="17" height="17" viewBox="0 0 24 24"><path fill="#f6c417" d="M12 2l3 6.5 7 .8-5.2 4.8 1.4 7L12 17.6 5.8 21l1.4-7L2 9.3l7-.8z"/></svg>
  <div class="logout">Logout</div>
</header>

<section class="hero">
  <div class="avatar" role="img" aria-label="Portrait photo of the mentor"></div>
  <div class="hero-name">Evan Marlow</div>
  <div class="hero-loc"><svg width="11" height="14" viewBox="0 0 12 16"><path fill="none" stroke="#fff" stroke-width="1.5" d="M6 15s5-5.5 5-9A5 5 0 0 0 1 6c0 3.5 5 9 5 9z"/><circle cx="6" cy="6" r="1.8" fill="#fff"/></svg>United States of America</div>
  <div class="hero-stars">
    <svg width="102" height="19" viewBox="0 0 110 20"><g fill="#f6c417"><path d="M10 1l2.6 5.6 6.1.7-4.5 4.2 1.2 6L10 14.6 4.6 17.5l1.2-6L1.3 7.3l6.1-.7z"/><path transform="translate(22)" d="M10 1l2.6 5.6 6.1.7-4.5 4.2 1.2 6L10 14.6 4.6 17.5l1.2-6L1.3 7.3l6.1-.7z"/><path transform="translate(44)" d="M10 1l2.6 5.6 6.1.7-4.5 4.2 1.2 6L10 14.6 4.6 17.5l1.2-6L1.3 7.3l6.1-.7z"/><path transform="translate(66)" d="M10 1l2.6 5.6 6.1.7-4.5 4.2 1.2 6L10 14.6 4.6 17.5l1.2-6L1.3 7.3l6.1-.7z"/><path transform="translate(88)" d="M10 1l2.6 5.6 6.1.7-4.5 4.2 1.2 6L10 14.6 4.6 17.5l1.2-6L1.3 7.3l6.1-.7z"/></g></svg>
    <span>5.0 (5 Reviews)</span>
  </div>
  <div class="hero-role">Director of Product - Hearthwell Insurance</div>
  <div class="spots">[2 SPOST AVAILABLE]</div>
  <div class="social" style="left:937px;top:90px;background:var(--blue)"><span></span></div>
  <div class="social" style="left:981px;top:90px;background:#1da1f2"><span></span></div>

  <div class="tab" style="left:336px;width:154px"><svg width="20" height="18" viewBox="0 0 22 20"><path fill="none" stroke="#9fb3c3" stroke-width="1.4" d="M2 2h18v12H9l-5 4v-4H2z"/><path stroke="#9fb3c3" d="M6 7h10M6 10h7"/></svg>Personal Chat</div>
  <div class="tab" style="left:507px;width:197px"><svg width="20" height="18" viewBox="0 0 22 20"><path fill="none" stroke="#9fb3c3" stroke-width="1.4" d="M6 2h10v5a5 5 0 0 1-10 0zM6 4H2c0 3 2 4 4 4M16 4h4c0 3-2 4-4 4M11 12v4M7 18h8"/></svg>Challenges &amp; Projects</div>
  <div class="tab" style="left:716px;width:163px"><svg width="18" height="20" viewBox="0 0 18 20"><rect x="2" y="2" width="14" height="17" rx="1" fill="none" stroke="#9fb3c3" stroke-width="1.4"/><path stroke="#9fb3c3" d="M5 7h8M5 10h8M5 13h5"/></svg>To-Dos &amp; Goals</div>
  <div class="tab" style="left:890px;width:145px"><svg width="18" height="18" viewBox="0 0 20 20"><path fill="none" stroke="#9fb3c3" stroke-width="1.4" d="M4 2l4 1 1 4-2 2a11 11 0 0 0 4 4l2-2 4 1 1 4-2 2C9 18 2 11 2 4z"/></svg>1- on-1 Calls</div>
</section>

<main>
<article class="card about">
  <p>Evan Marlow is passionate about creating and scaling powerful web and mobile products that make a significant impact in millions of people's lives around the world. Evan deeply enjoys building and managing the product and development teams that help achieveth at goal.</p>
  <p>Evan is currently the Director of Product at Hearthwell Insurance (<a>www.hearthwell.example</a>). He was previously the CPO of Lumen Ad Media (<a>www.lumenad.example</a>) which operated in the Ad Tech industry, helping the world's largest media companies with data- inspired storytelling. Previously a Senior Product leader at Skyway Travel (<a>www.skyway.example</a>) and Printloom Digital (<a>www.printloom.example/digital</a>).</p>

  <div class="t-head"><div class="t-badge">Testimonials</div><div class="t-rule"></div></div>

  <p class="quote">"Evan helped me set focus and intention in my goal of scaling my independent projects. Before working with Evan I felt like I was jumping from idea to idea with no plan. During our session he proved clear action items which I enjoyed completing. Each week were viewed the progress and established new items to iterate towards my goal. I am very thank ful for my mentoring sessions with Evan "</p>
  <div class="quote-by">Mara</div>

  <p class="quote">"Evan has been a fantastic coach. I Signed up for 1:1 interview prep with Evan. from the get-go, Evan was invested in helping me land my next product role. He helped me polish my Stories, deliver My responses more effectively and prepare for any curveball Questions during my interviews. As a successful product leader, he bring tons of deep industry knowledge which I found invaluable for my preparation. However, What sets Evan apart is that he's a mentor, a cheerleader and a friend all rolled into one. I highly recommend Evan Marlow to anyone looking for a mentor in the product space. "</p>
  <div class="quote-by">Aarav</div>

  <p class="quote">"Evan was careful to understand our issue and was open about his prior experience working in the same space. It was great to bounce ideas off him and get some encouraging feedback to keep moving forward.</p>
  <div class="quote-by">Tobias</div>

  <p class="quote">"Evan is obviously a master artist when it comes to growth and growth hacking. He Quickly distilled the key points that I needed work on and provided super insights. Most importantly, he went above and beyond by sending follow-up suggestions and action items, demonstrating his intrest and kindness in helping me. I would highly recommend Evan to anyone working on initial p/m strategies.</p>
  <div class="quote-by">Reid</div>

  <div class="promo">
    <div class="lead">Aspiring or new PM? Or looking to level up ?</div>
    <div>Check out my new Product Management course here:</div>
    <a>www.pmcraftcourse.example</a>
    <div>(Use 25 PCT TO &nbsp;FFMENTOR for 25 % off my Course!)</div>
  </div>

  <div class="links">
    <div>Author: Shipping Useful Products</div>
    <a>(www.shippingusefulproducts.example)</a>
    <div class="gap"></div>
    <div>Author: Reinventing Your Path</div>
    <a>(www.reinventyourpath.example)</a>
    <div class="gap"></div>
    <div style="font-size:13.5px">Website: &nbsp;<a style="font-size:12px">www.craftofproduct.example</a></div>
    <div class="gap"></div>
    <div style="font-size:13.5px">Blog: &nbsp;<a style="font-size:12px">https://inkwell.example/@emarlow</a></div>
    <div>Top Write in Inkwell startup Category</div>
    <a>(https://inkwell.example/tag/startup/top-writers)</a>
    <div class="gap"></div>
    <div style="line-height:19px">The Craft of Product Newsletter:<br><a>https://link.example/CPnewsletter</a><br>The Craft of Product Video Channel:<br><a>https://video.example/channel/cp-7Hq2LmX9aRt4KwB3</a></div>
  </div>
</article>

<div class="card rev" style="top:2089px;height:207px">
  <p>Evan helped me set focus and intention in my goal of scaling my independent projrect. Before working with Evan, I felt like I Was jumping from idea to idea with no plan. During our sesion he provided clear action items which I enjoyed completing. Each week we revied the progress and Established new items to iterate towards my goal. i am very thankful for my mentoring sessions with Evan.</p>
  <div class="rev-by"><svg width="20" height="18" viewBox="0 0 20 18"><path fill="#2c3a4f" d="M1 8h4v10H1zM6 8l4-7c2 0 2.5 1.5 2 3l-1 3h6c1.5 0 2 1 1.8 2l-1.5 7c-.2 1-1 2-2 2H6z"/></svg>Testimonial by Mara from September 2020</div>
</div>
<div class="card rev" style="top:2320px;height:229px">
  <p>Evan is a fantastic mentor and I definitely recommaend him to any Product manger or aspiring PMs. Evan Worked with men on my resume since I wasn't getteing any callbacks. the results were almost instantaneous as I got my 1st Callback from a Recruiter after only 2 hours of applying with the resume he helped me with. I can't Recommend Evan enough.</p>
  <div class="rev-by"><svg width="20" height="18" viewBox="0 0 20 18"><path fill="#2c3a4f" d="M1 8h4v10H1zM6 8l4-7c2 0 2.5 1.5 2 3l-1 3h6c1.5 0 2 1 1.8 2l-1.5 7c-.2 1-1 2-2 2H6z"/></svg>Testimonial by Amir from September 2020</div>
</div>
<div class="card rev" style="top:2574px;height:208px">
  <p>Before Working with Evan, I felt like I was jumping from idea to idea with no plan. During our session he proved clear action items which I enjoyed completing. each week We reviewed the progress and established new items to iterate towards my goal. i am very thankful for my mentoring sessions with Evan.</p>
  <div class="rev-by"><svg width="20" height="18" viewBox="0 0 20 18"><path fill="#2c3a4f" d="M1 8h4v10H1zM6 8l4-7c2 0 2.5 1.5 2 3l-1 3h6c1.5 0 2 1 1.8 2l-1.5 7c-.2 1-1 2-2 2H6z"/></svg>Testimonial by Mara From October 2020</div>
</div>

<aside>
  <div class="card side" style="top:390px;height:326px">
    <div style="display:flex;align-items:center;gap:6px;color:var(--blue);font-size:12px"><svg width="13" height="13" viewBox="0 0 14 14"><path fill="#2f8cf0" d="M1 1h6l6 6-6 6-6-6z"/><circle cx="4" cy="4" r="1.2" fill="#fff"/></svg>7 Day Trial !</div>
    <div style="margin-top:6px;font-size:37px;font-weight:600;color:#2c4a6a;line-height:44px">$240/<span style="font-size:22px;color:var(--teal);font-weight:500">mo</span></div>
    <h3 style="margin-top:18px">Personal Mentorship</h3>
    <div class="small" style="margin-top:10px">Continuos and personal 1-to-1 Mentorship for a flat fee.</div>
    <div style="margin-top:22px;color:var(--teal);font-size:15.5px;font-weight:500;text-decoration:underline">What's Included ?</div>
    <div class="btn" style="margin-top:20px;width:187px">Apply For mentorship</div>
  </div>

  <div class="card side" style="top:738px;height:193px">
    <h3>"Other(60MinuteSession) "Session</h3>
    <div class="small" style="margin-top:14px">60 minutes, $150 per session</div>
    <div class="btn" style="margin-top:18px;width:134px">Book Session</div>
  </div>

  <div class="card side" style="top:955px;height:246px">
    <h3>" How to Become a Products Manager - Coaching Seeion (60 Minutes Session)</h3>
    <div class="small" style="margin-top:16px">60 minutes, $150 per session</div>
    <div class="btn" style="margin-top:18px;width:134px">Book Session</div>
  </div>

  <div class="abs" style="left:834px;top:1242px;display:flex;align-items:center;gap:8px;color:var(--ink);font-size:13px;font-weight:500"><span style="text-decoration:underline">Shaow All Sessions</span><svg width="28" height="8" viewBox="0 0 28 8"><path fill="none" stroke="#1bd0b2" d="M0 4h26M22 1l4 3-4 3"/></svg></div>

  <div class="card side" style="top:1301px;height:155px">
    <h3>Average Response Time</h3>
    <div style="display:flex;gap:8px;margin-top:12px"><svg width="12" height="20" viewBox="0 0 12 20"><path fill="#1bd0b2" d="M7 0L0 12h5l-2 8 9-13H7z"/></svg><div class="small">Usually Responds with in a few hours</div></div>
  </div>

  <div class="card side" style="top:1477px;height:156px">
    <h3>Part of These groups</h3>
    <div style="display:flex;gap:6px;align-items:center;margin-top:14px;color:var(--teal);font-size:13px"><svg width="14" height="14" viewBox="0 0 16 16"><path fill="none" stroke="#1bd0b2" stroke-width="1.6" d="M7 9a3 3 0 0 0 4 0l3-3a3 3 0 0 0-4-4L9 3M9 7a3 3 0 0 0-4 0L2 10a3 3 0 0 0 4 4l1-1"/></svg>Mentors For Startups</div>
  </div>

  <div class="card side" style="top:1654px;height:844px">
    <h3>Skill Taught By Mentor</h3>
    <ul class="skills">
      <li>Product &amp; Marketing</li><li>Product</li><li>Product Manager</li><li>Interview</li>
      <li>StartUp &nbsp;&nbsp;&nbsp;&nbsp;&nbsp;&nbsp;&nbsp;&nbsp;&nbsp;&nbsp;&nbsp;&nbsp;Tech</li><li>Media</li><li>Interview &nbsp;&nbsp;&nbsp;&nbsp;&nbsp;&nbsp;&nbsp;&nbsp;&nbsp;Pm</li>
      <li>Project Manger</li><li>Project Management</li><li>Interview Prep</li><li>Mock Interview</li>
      <li>Product interview</li><li>Product Market Fit</li><li>Product Pricing</li><li>Associate Product Manager</li>
      <li>Junior Product Manager</li><li>New Product Manger</li><li>B2b &nbsp;&nbsp;&nbsp;&nbsp;B2c</li>
      <li>Mobile Apps &nbsp;&nbsp;&nbsp;&nbsp;&nbsp;&nbsp;&nbsp;&nbsp;&nbsp;&nbsp;Ios</li><li>Android</li>
    </ul>
  </div>
</aside>

<h2 class="related-title">Related Mentors</h2>
<div class="card mentor" style="left:165px">
  <div class="avatar" role="img" aria-label="Portrait photo of Owen Rivera"></div>
  <div class="mentor-name">Owen Rivera</div>
  <div class="mentor-role">Product Manager</div>
  <div class="price">$180<br>Per<br>Month</div>
  <div class="mentor-copy">We believe Owen could be a good match for you too.</div>
  <ul class="mentor-list"><li>Minimal Viable Products</li><li>Team Leadership</li><li>Architecture</li><li>Web Development</li></ul>
</div>
<div class="card mentor" style="left:475px">
  <div class="avatar" role="img" aria-label="Portrait photo of Kofi Adeyemi" style="background:linear-gradient(145deg,#8a5a3c,#4a2e20)"></div>
  <div class="mentor-name">Kofi Adeyemi</div>
  <div class="mentor-role">Software Product<br>Manager</div>
  <div class="price">$140<br>per<br>month</div>
  <div class="mentor-copy">We believe Kofi could be a good match for you too.</div>
  <ul class="mentor-list"><li>Remote Work</li><li>Agile Product Mangement</li><li>Product Development lifecycle</li><li>Freelance Pm</li><li>Team Collection</li></ul>
</div>
</main>

<footer class="footer">
  <div class="brand" style="top:46px"><div class="brand-dot"></div><span class="brand-name" style="color:#fff">Mentor Harbor</span></div>
  <p class="abs" style="left:61px;top:104px;width:250px;line-height:20px">Your trusted source to find highly - vetted mentors &amp; industry professionals to move your career ahead.</p>
  <div class="abs" style="left:61px;top:171px;display:flex;gap:10px;align-items:center"><svg width="16" height="12" viewBox="0 0 16 12"><rect width="16" height="12" rx="1" fill="#1bd0b2"/><path fill="none" stroke="#2f3b57" stroke-width="1.3" d="M1 1l7 5 7-5"/></svg>hello@mentorharbor.example</div>
  <div class="abs" style="left:61px;top:200px;font-size:11px">©<span style="color:var(--teal)">Mentor Harbor</span> - All Rights Reserved.</div>

  <h4 style="left:424px">Sitemap</h4>
  <ul style="left:424px"><li>Browse</li><li>Mentors</li><li>Become A mentor</li><li>Partner</li><li>Program</li><li>Faq</li><li>Blog</li></ul>
  <h4 style="left:677px">Quick Links</h4>
  <ul style="left:681px"><li>About Us</li><li>Code Of Conduct</li><li>Privacy Policy</li><li>Success Stories</li></ul>
  <h4 style="left:923px">Follow Us</h4>
  <div class="social" style="left:918px;top:82px;background:var(--blue)"><span></span></div>
  <div class="social" style="left:962px;top:82px;background:#1da1f2"><span></span></div>
</footer>
<div class="footstrip"></div>
<svg class="abs" style="left:591px;top:3543px" width="18" height="9" viewBox="0 0 18 9"><path fill="#1bd0b2" d="M0 9L9 0l9 9z"/></svg>

</body>
</html>
```